I will ask the design of the business card

We are looking for business card design of the new company "TORVIK QUANTA WORKS LLC." Based in Azerbaijan.
In case
We are working on Azerbaijan to set up the first exchange of crypto currencies.

The key currency used in exchanges is called "MELDA".
In case
We are doing project to make crypto currency infrastructure.

We provide state-of-the-art technology to the world.

```html
<!DOCTYPE html>
<html lang="en">
<head>
<meta charset="utf-8">
<title>Torvik Quanta Works LLC. — Business Card</title>
<link rel="stylesheet" href="https://fonts.googleapis.com/css2?family=Montserrat:wght@300;400;500;600&family=Roboto:wght@400;500&display=swap">
<style>
  :root {
    --backdrop: #d3d7d7;
    --paper: #f6f6f5;
    --edge-blue: #1b5fc0;
    --ink: #3b3b3d;
    --ink-soft: #55575a;
    --night: #1b1b1c;
    --night-cell: #343537;
    --brand-blue: #1f7cc4;
    --brand-blue-deep: #1a6fb8;
    --cell-blue: #45aee2;
    --accent-blue: #3aa2e2;
    --divider: rgba(255,255,255,0.35);
    --white: #ffffff;
  }
  * { box-sizing: border-box; margin: 0; padding: 0; }
  html, body { width: 1200px; height: 1050px; overflow: hidden; }
  body {
    background: var(--backdrop);
    font-family: "Montserrat", sans-serif;
    position: relative;
  }
  .card {
    position: absolute;
    top: 175px;
    width: 400px;
    height: 700px;
    background: var(--paper);
    border-bottom: 5px solid var(--edge-blue);
    box-shadow: 0 14px 30px rgba(0,0,0,0.18);
    overflow: hidden;
  }
  .card--front { left: 150px; }
  .card--back { left: 650px; }

  /* Front: brand area */
  .brand {
    height: 290px;
    display: flex;
    align-items: center;
    gap: 22px;
    padding: 0 34px;
  }
  .brand__dot {
    width: 56px; height: 56px; border-radius: 50%;
    background: var(--brand-blue-deep);
    flex: none;
  }
  .brand__name {
    font-weight: 600;
    font-size: 27px;
    line-height: 1.15;
    color: var(--ink);
    letter-spacing: 0.5px;
  }

  /* Front: contact rows */
  .contact-row {
    display: flex;
    height: 102px;
    border-top: 1px solid var(--divider);
  }
  .contact-row:first-child { border-top: none; }
  .contact-row__icon {
    width: 92px; flex: none;
    display: flex; align-items: center; justify-content: center;
    background: var(--cell-blue);
    border-right: 1px solid var(--divider);
  }
  .contact-row__text {
    flex: 1;
    background: var(--brand-blue);
    color: var(--white);
    display: flex; flex-direction: column; justify-content: center;
    padding-left: 26px;
    font-size: 15px;
    line-height: 1.45;
    letter-spacing: 0.6px;
  }
  .contact-row--person .contact-row__icon { background: var(--night-cell); border-right: none; }
  .contact-row--person .contact-row__text { background: var(--night); }
  .person__name { font-size: 30px; font-weight: 500; letter-spacing: 1.5px; line-height: 1.1; }
  .person__role { font-size: 13px; color: var(--accent-blue); letter-spacing: 1.6px; margin-top: 4px; }
  .contact-row svg { width: 34px; height: 34px; fill: none; stroke: var(--white); stroke-width: 2; }
  .contact-row--person svg { fill: var(--white); stroke: none; }

  /* Back */
  .card--back {
    display: flex; flex-direction: column; align-items: center; justify-content: center;
  }
  .wordmark { display: flex; align-items: center; gap: 16px; }
  .wordmark__dot { width: 40px; height: 40px; border-radius: 50%; background: var(--brand-blue-deep); }
  .wordmark__name {
    font-weight: 300; font-size: 66px; letter-spacing: 2px; color: var(--brand-blue);
  }
  .tagline {
    margin-top: 14px;
    font-family: "Roboto", sans-serif;
    font-size: 14px; line-height: 1.35; text-align: center;
    color: var(--ink-soft);
  }
</style>
</head>
<body>
  <section class="card card--front">
    <header class="brand">
      <span class="brand__dot"></span>
      <h1 class="brand__name">TORVIK QUANTA<br>WORKS LLC.</h1>
    </header>
    <div class="contact">
      <div class="contact-row contact-row--person">
        <div class="contact-row__icon">
          <svg viewBox="0 0 34 34" aria-hidden="true"><circle cx="17" cy="11" r="7"/><path d="M5 31c0-8 5-12 12-12s12 4 12 12z"/></svg>
        </div>
        <div class="contact-row__text">
          <p class="person__name">Elin Varga</p>
          <p class="person__role">MANAGING DIRECTOR</p>
        </div>
      </div>
      <div class="contact-row">
        <div class="contact-row__icon">
          <svg viewBox="0 0 34 34" aria-hidden="true"><rect x="9" y="4" width="16" height="26" rx="2"/><line x1="9" y1="25" x2="25" y2="25"/></svg>
        </div>
        <div class="contact-row__text"><p>+994 12 480 3317</p><p>+994 50 612 2045</p></div>
      </div>
      <div class="contact-row">
        <div class="contact-row__icon">
          <svg viewBox="0 0 34 34" aria-hidden="true"><circle cx="17" cy="17" r="12"/><ellipse cx="17" cy="17" rx="5" ry="12"/><line x1="5" y1="17" x2="29" y2="17"/><line x1="7" y1="11" x2="27" y2="11"/><line x1="7" y1="23" x2="27" y2="23"/></svg>
        </div>
        <div class="contact-row__text"><p>info@torvikquanta.az</p><p>www.torvikquanta.az</p></div>
      </div>
      <div class="contact-row">
        <div class="contact-row__icon">
          <svg viewBox="0 0 34 34" aria-hidden="true"><path d="M4 17 17 6l13 11"/><path d="M8 14v14h18V14"/><rect x="14" y="19" width="6" height="9"/></svg>
        </div>
        <div class="contact-row__text"><p>AZ1010, 27/4B, Arzuman Str.</p><p>Baku City, Azerbaijan</p></div>
      </div>
    </div>
  </section>

  <section class="card card--back">
    <div class="wordmark">
      <span class="wordmark__dot"></span>
      <h2 class="wordmark__name">MELDA</h2>
    </div>
    <p class="tagline">Decentralized value exchange<br>platform for Real Business Market</p>
  </section>
</body>
</html>
```